Instructions for nurses on how to give a report on each shift

I have a 2-page reference sheet that needs to be updated to look more aesthetically pleasing.

Target Market(s)

Healthcare, nurses

Industry/Entity Type

Healthcare

Font styles to use
Sans Serif

Requirements
Must have
• Please make sure it is easy to read, the content is well organized and has a flow to it. Please also pick colors that would coordinate with our website www.ovtrime.org (so mainly navy and white or off-white with accent colors.) Please make sure to add accent colors to break up the content. The BORSK name and title at the top should remain on the page but I'm not married to the star or logo style. You can do what you think looks best there. Way at the bottom in fine print, I would like for you to add OVTRIME © 2019 All rights reserved.

```html
<!DOCTYPE html>
<html lang="en">
<head>
<meta charset="utf-8">
<title>BORSK Shift Report Reference</title>
<link rel="stylesheet" href="https://fonts.googleapis.com/css2?family=Roboto:wght@400;500;700&family=Open+Sans:wght@400;600;700&display=swap">
<style>
:root{
  --bg:#6a6a6a;
  --paper:#ffffff;
  --navy:#0e3a62;
  --navy-dark:#0a2c4b;
  --pale:#cfdbe8;
  --panel:#e9e9ea;
  --brand:#4a78a8;
  --muted:#5a6b7c;
  --ink:#1d2a36;
  --line:#555;
}
*{box-sizing:border-box;margin:0;padding:0}
html,body{width:1200px;height:1200px;overflow:hidden;background:var(--bg);font-family:"Open Sans",sans-serif;color:var(--ink)}
.page{position:absolute;left:250px;width:700px;height:544px;background:var(--paper)}
.page-one{top:42px}
.page-two{top:614px}
.abs{position:absolute}
.brand{position:absolute;left:32px;top:34px}
.brand-name{display:flex;align-items:center;gap:6px;font-family:"Roboto",sans-serif;font-weight:500;font-size:20px;color:var(--brand);letter-spacing:1px}
.brand-name .mark{width:12px;height:12px;background:#8fb0d0}
.brand-title{font-family:"Open Sans",sans-serif;font-weight:400;font-size:9.5px;color:var(--muted);line-height:13px;margin-top:4px;width:190px}
.leader{left:249px;top:78px;width:201px;height:85px;background:var(--navy);color:#fff;font-family:"Roboto",sans-serif;padding:6px 6px}
.leader h2{text-align:center;font-size:15px;font-weight:500;letter-spacing:.5px;margin-bottom:4px}
.leader .row{display:flex;font-size:10.5px;line-height:17px}
.leader .row span{width:72px}
.leader .row i{flex:1;border-bottom:1px solid #9fb5cc;height:11px}
.q{width:114px;height:76px;background:var(--navy);color:#fff;font-size:6.4px;padding:5px 6px;line-height:8px;overflow:hidden}
.q b{font-weight:600;display:block;margin-bottom:4px}
.q ul{list-style:none;display:grid;grid-template-columns:1fr;row-gap:4px}
.q ul.two{grid-template-columns:1fr 1fr;grid-auto-flow:column;column-gap:4px}
.q li{font-weight:600;white-space:nowrap}
.q li::before{content:"● ";font-size:5px;vertical-align:1px}
.ans{width:100px;background:var(--pale);border-left:2px solid #333;border-bottom:2px solid #333;font-size:6.4px;text-align:center;color:var(--navy-dark);line-height:9.4px;padding:8px 4px}
.ans.no{height:69px}
.ans.yes{height:88px;padding-top:6px}
.ans .fill{text-align:left;margin-top:5px}
.ans .fill div{border-bottom:1px solid #666;height:11px;font-size:6px;line-height:10px}
.copyright{position:absolute;right:20px;font-size:7.4px;color:#333;font-family:"Roboto",sans-serif}
.headline{left:248px;top:64px;font-family:"Roboto",sans-serif;font-weight:500;font-size:17px;line-height:21.5px;color:var(--navy)}
.section{position:absolute;background:var(--panel)}
.section h3{background:var(--navy);color:#fff;font-family:"Roboto",sans-serif;font-weight:500;font-size:14px;height:32px;line-height:32px;padding-left:10px}
.section ul,.tips ul{list-style:none;font-size:8.2px;line-height:15.6px;padding:8px 0 0 12px}
.section li,.tips li{padding-left:10px;position:relative}
.section li::before,.tips li::before{content:"";position:absolute;left:0;top:5px;width:5px;height:5px;border-radius:50%;background:#333}
.tips li{line-height:11.2px;margin-bottom:4.4px}
.tips h4{font-family:"Roboto",sans-serif;font-weight:500;color:var(--navy);font-size:12px;margin-bottom:5px}
</style>
</head>
<body>

<section class="page page-one">
  <div class="brand">
    <div class="brand-name"><span class="mark"></span>BORSK</div>
    <div class="brand-title">Shift Report Reference Guide<br>for Nursing Teams</div>
  </div>

  <div class="abs leader">
    <h2>LEADER</h2>
    <div class="row"><span>Name:</span><i></i></div>
    <div class="row"><span>Title:</span><i></i></div>
    <div class="row"><span>Assignment:</span><i></i></div>
  </div>

  <svg class="abs" style="left:0;top:0" width="700" height="544" aria-hidden="true">
    <defs><marker id="arr" markerWidth="6" markerHeight="6" refX="3" refY="5" orient="auto"><path d="M0,0 L6,0 L3,6z" fill="#333"/></marker></defs>
    <g stroke="var(--line)" stroke-width="0.8" stroke-dasharray="2 2" fill="none">
      <line x1="351" y1="163" x2="351" y2="177" marker-end="url(#arr)"/>
      <line x1="94" y1="187" x2="609" y2="187"/>
      <line x1="94" y1="187" x2="94" y2="225" marker-end="url(#arr)"/>
      <line x1="222" y1="187" x2="222" y2="225" marker-end="url(#arr)"/>
      <line x1="351" y1="187" x2="351" y2="225" marker-end="url(#arr)"/>
      <line x1="481" y1="187" x2="481" y2="225" marker-end="url(#arr)"/>
      <line x1="609" y1="187" x2="609" y2="225" marker-end="url(#arr)"/>
      <line x1="94" y1="308" x2="94" y2="324" marker-end="url(#arr)"/>
      <line x1="222" y1="308" x2="222" y2="324" marker-end="url(#arr)"/>
      <line x1="351" y1="308" x2="351" y2="324" marker-end="url(#arr)"/>
      <line x1="481" y1="308" x2="481" y2="324" marker-end="url(#arr)"/>
      <line x1="609" y1="308" x2="609" y2="324" marker-end="url(#arr)"/>
      <polyline points="76,308 76,322 38,322 38,410" marker-end="url(#arr)"/>
      <polyline points="206,308 206,322 168,322 168,410" marker-end="url(#arr)"/>
      <polyline points="334,308 334,322 296,322 296,410" marker-end="url(#arr)"/>
      <polyline points="465,308 465,322 427,322 427,410" marker-end="url(#arr)"/>
      <polyline points="592,308 592,322 554,322 554,410" marker-end="url(#arr)"/>
    </g>
  </svg>

  <div class="abs q" style="left:37px;top:232px"><b>Any change in resident status?</b>
    <ul><li>Admissions</li><li>Discharges</li><li>Transfers</li><li>Appointments</li></ul></div>
  <div class="abs q" style="left:166px;top:232px"><b>Any concerning changes in resident's condition?</b>
    <ul class="two" style="grid-template-rows:repeat(4,auto)"><li>Pain</li><li>Skin</li><li>Ambulation</li><li>Safety</li><li>Behavior</li><li>Appetite</li><li>Elimination</li></ul></div>
  <div class="abs q" style="left:295px;top:232px"><b>Any residents requiring extraordinary monitoring?</b>
    <ul><li>Falls</li><li>Decline in condition</li><li>IV/ABT therapy</li><li>Hospice</li></ul></div>
  <div class="abs q" style="left:423px;top:232px"><b>Any concerns related to residents environment?</b>
    <ul><li>Room temperature</li><li>Supplies</li><li>Equipment</li></ul></div>
  <div class="abs q" style="left:548px;top:232px"><b style="margin-bottom:3px">Any concerns or barriers related to your ability to perform your job effectively?</b>
    <ul class="two" style="grid-template-rows:repeat(3,auto);row-gap:3px"><li>Supplies</li><li>Time constraints</li><li>Family requests</li><li>Acuity</li><li>Environment</li></ul></div>

  <div class="abs ans no" style="left:46px;top:331px">NO<br>"I do not have any actual or expected changes in resident status."</div>
  <div class="abs ans no" style="left:175px;top:331px">NO<br>"I have no residents requiring extraordinary monitoring."</div>
  <div class="abs ans no" style="left:303px;top:331px">NO<br>"I have no concerns related to my residents environment."</div>
  <div class="abs ans no" style="left:433px;top:331px">NO<br>"I do not have any actual or expected changes in resident status."</div>
  <div class="abs ans no" style="left:562px;top:331px">NO<br>"I have no concerns or barriers affecting my ability to perform my job."</div>

  <div class="abs ans yes" style="left:46px;top:415px">YES<br>"My residents with changes in their status are…"<div class="fill"><div>1</div><div>2</div><div>3</div></div></div>
  <div class="abs ans yes" style="left:175px;top:415px">YES<br>"My residents w/ concerning changes in their condition include…"<div class="fill"><div>1</div><div>2</div><div>3</div></div></div>
  <div class="abs ans yes" style="left:303px;top:415px">YES<br>"My residents that require extraordinary monitoring are…"<div class="fill"><div>1</div><div>2</div><div>3</div></div></div>
  <div class="abs ans yes" style="left:433px;top:415px">YES<br>"My residents with concerns related to their environment include…"<div class="fill"><div>1</div><div>2</div><div>3</div></div></div>
  <div class="abs ans yes" style="left:562px;top:415px">YES<br>"My concerns affecting my ability to perform my job include…"<div class="fill"><div>1</div><div>2</div><div>3</div></div></div>

  <p class="copyright" style="top:519px">OVTRIME © 2019 All rights reserved.</p>
</section>

<section class="page page-two">
  <div class="brand" style="left:30px;top:28px">
    <div class="brand-name" style="font-size:17px"><span class="mark"></span>BORSK</div>
    <div class="brand-title" style="font-size:8.5px;line-height:11px">Shift Report Reference Guide<br>for Nursing Teams</div>
  </div>
  <h1 class="abs headline">When "I" is replaced by "WE"<br>Even illness becomes wellness.</h1>

  <div class="section" style="left:20px;top:124px;width:327px;height:128px">
    <h3>OBJECTIVES:</h3>
    <ul><li>Accountability: Declare roles and assignments</li><li>Advocacy: Identify patient needs</li><li>Critical Thinking: Prioritize and recognize obstacles</li><li>Communication: Share important information</li><li>Collaboration: Utilize an interdisciplinary approach</li></ul>
  </div>
  <div class="section" style="left:351px;top:124px;width:329px;height:128px">
    <h3>OUTCOMES:</h3>
    <ul><li>Share best practices</li><li>Improve communication</li><li>Promote cohesiveness</li><li>Increase staff morale</li><li>Enhance patient and organizational outcomes</li></ul>
  </div>
  <div class="section" style="left:20px;top:258px;width:327px;height:142px">
    <h3>WHO:</h3>
    <ul><li>All nurses on the unit</li><li>All nursing support staff (CNA/MA/HCT)</li><li>Administrator</li><li>Director of Nursing</li><li style="line-height:11.5px">Head of pertinent disciplines (Dietary, Social Work, Physical Therapy, Engineering, Central Supply, etc.)</li></ul>
  </div>
  <div class="section" style="left:351px;top:258px;width:329px;height:76px">
    <h3>WHEN:</h3>
    <ul><li>Every morning (assign a meeting time for each unit)</li><li>Keep meetings within 15 minutes in length</li></ul>
  </div>
  <div class="section" style="left:351px;top:340px;width:329px;height:60px">
    <h3>WHERE:</h3>
    <ul><li>Nursing station on each unit</li></ul>
  </div>

  <div class="abs tips" style="left:28px;top:418px;width:340px">
    <h4>HELPFUL TIPS:</h4>
    <ul style="padding:0"><li>Assign a meeting facilitator (usually the administrator of the facility)</li><li>Standing during meetings keeps the meetings short and to the point</li><li>Keeping meetings within 15 minutes emphasizes being prepared and direct</li><li>Keep meeting times consistent (morning is best)</li><li>Do not begin until everyone is present (minimizes stragglers)</li><li>Avoid discussing personal concerns</li></ul>
  </div>
  <div class="abs tips" style="left:366px;top:432px;width:310px">
    <ul style="padding:0"><li>Include reminders for in-services, meetings, etc. and updates towards the end of the meeting</li><li>Always conclude with achievements, milestones, praise, words of encouragement, motivational quote, etc.</li></ul>
  </div>

  <p class="copyright" style="top:520px">OVTRIME © 2019 All rights reserved.</p>
</section>

</body>
</html>
```